依頼詳細
ファクタリングは貸金業ではないのですが、資金の調達という特性上、怖い・嫌だなど嫌悪感を与えないようなデザイン、年齢層は、30代から70代の男女ですが、事業主相手なので、多少高級感を出してください。
記載項目
さくらもち舎 https://sakuramochisha.example
内のロゴ、トップページの画像を利用してください。
サイズ
• 新聞広告 半五段
希望イメージ
シンプル 複雑
単色 カラフル
暗い 明るい
日常 高級
遊び心 厳粛
未来的 伝統的
女性的 男性的
希望する色
モノクロ

```html
<!DOCTYPE html>
<html lang="ja">
<head>
<meta charset="utf-8">
<title>さくらもち舎 ファクタリング 新聞広告</title>
<link rel="stylesheet" href="https://fonts.googleapis.com/css2?family=Noto+Sans+JP:wght@400;500;700;900&display=swap">
<style>
:root{
  --ink:#1a1a1a;
  --ink-soft:#4a4a4a;
  --gray-dark:#5a5a5a;
  --gray-mid:#a9a9a9;
  --gray-light:#dcdcdc;
  --paper:#ffffff;
}
*{margin:0;padding:0;box-sizing:border-box}
html,body{width:851px;height:1200px;overflow:hidden;background:var(--paper)}
body{font-family:"Noto Sans JP",sans-serif;color:var(--ink);position:relative}
.ad{position:absolute;left:48px;top:220px;width:755px;height:760px;border:1px solid var(--gray-mid);background:var(--paper);overflow:hidden}
.abs{position:absolute}
.hero{left:0;top:0;width:755px;height:320px;background:linear-gradient(180deg,#b8b8b8 0%,#d6d6d6 55%,#ececec 100%)}
.hero-photo{left:450px;top:24px;width:170px;height:296px;background:linear-gradient(180deg,#8c8c8c,#5e5e5e);border-radius:85px 85px 0 0}
.hero-lead{left:30px;top:28px;width:400px;color:var(--gray-dark);font-weight:500;font-size:28px;line-height:1.3}
.pill{left:22px;top:172px;padding:2px 12px;background:var(--ink);color:var(--paper);font-weight:900;font-size:22px;border-radius:22px;line-height:1.4}
.head-1{left:118px;top:160px;font-weight:900;font-size:44px;line-height:1.1;white-space:nowrap}
.head-2{left:14px;top:226px;font-weight:900;font-size:46px;line-height:1.2;letter-spacing:-2px;white-space:nowrap}
.head-2 .mark{background:var(--paper);padding:0 2px}
.bubble{display:flex;align-items:center;justify-content:center;text-align:center;width:140px;height:70px;background:var(--paper);border:1.5px solid var(--ink-soft);border-radius:50%;font-size:11.5px;font-weight:500;line-height:1.35;padding:0 12px}
.arrow{left:150px;top:328px}
.factoring{left:18px;top:380px;padding:2px 8px;border:3px solid var(--ink);font-weight:900;font-size:42px;line-height:1.15;letter-spacing:-2px;white-space:nowrap}
.system{left:16px;top:446px;font-weight:900;font-size:48px;line-height:1.2;white-space:nowrap}
.tag{left:358px;top:448px;width:86px;padding:5px 4px;background:var(--ink);color:var(--paper);font-weight:700;font-size:14px;line-height:1.3;text-align:center}
.intro{left:462px;top:334px;width:280px;font-size:11px;line-height:1.6;color:var(--ink-soft)}
.features-title{left:462px;top:412px;width:280px;text-align:center;font-weight:900;font-size:18px}
.features{left:462px;top:442px;width:280px;display:flex;justify-content:space-between}
.feature{width:82px;height:82px;border-radius:50%;border:2px solid var(--ink);display:flex;flex-direction:column;align-items:center;justify-content:center;text-align:center;font-weight:700;font-size:12px;line-height:1.25}
.feature strong{font-size:19px;font-weight:900}
.scheme{left:16px;top:522px;width:420px;height:118px}
.office-photo{left:462px;top:538px;width:280px;height:102px;background:linear-gradient(135deg,#d2d2d2,#9a9a9a)}
.brand-strip{left:462px;top:612px;width:280px;height:28px;background:rgba(255,255,255,.88);display:flex;align-items:center;justify-content:center;gap:8px;font-weight:700;font-size:14px}
.brand-strip .dot{width:10px;height:10px;border-radius:50%;background:var(--ink)}
.footer-rule{left:16px;top:654px;width:726px;height:1px;background:var(--gray-mid)}
.company{left:18px;top:664px;font-weight:900;font-size:25px;line-height:1.3}
.company small{font-size:15px;font-weight:700}
.address{left:18px;top:712px;font-size:11px;color:var(--ink-soft)}
.contact-band{left:462px;top:664px;width:280px;padding:3px 0;background:var(--ink);color:var(--paper);text-align:center;font-size:13px;font-weight:700;letter-spacing:2px}
.phone{left:462px;top:692px;width:280px;text-align:center;font-weight:700;font-size:38px;line-height:1.1;letter-spacing:1px}
</style>
</head>
<body>
<div class="ad">
  <section class="abs hero"></section>
  <div class="abs hero-photo" role="img" aria-label="資金繰りに悩むスーツ姿のビジネスマンの写真"></div>
  <p class="abs hero-lead">あなたのビジネスを<br>てつだいたい!!</p>
  <span class="abs pill">しかも</span>
  <h1 class="abs head-1">事業資金を</h1>
  <h2 class="abs head-2"><span class="mark">「借りず」</span>に調達!</h2>

  <p class="abs bubble" style="left:440px;top:44px">融資が遅れたため、<br>間に合わない…</p>
  <p class="abs bubble" style="left:440px;top:196px">融資の審査が<br>不安だなぁ…</p>
  <p class="abs bubble" style="left:606px;top:44px">銀行の融資を<br>断られてしまった…</p>
  <p class="abs bubble" style="left:606px;top:196px">追加で資金が<br>必要になった…</p>

  <svg class="abs arrow" width="60" height="50" viewBox="0 0 60 50" aria-hidden="true">
    <path d="M20 2 H40 V24 H56 L30 48 L4 24 H20 Z" fill="none" stroke="#1a1a1a" stroke-width="3"/>
  </svg>

  <div class="abs factoring">「ファクタリング」</div>
  <div class="abs system">システムです。</div>
  <div class="abs tag">貸金業では<br>ありません</div>

  <p class="abs intro">企業様が保有している売掛金をファクタリング会社が買い取ることにより、支払期日より前に現金化できます。借入ではないため、決算書への影響もありません。</p>
  <p class="abs features-title">3つの特長!!</p>
  <div class="abs features">
    <div class="feature">最短<strong>1日</strong>即日入金</div>
    <div class="feature">融資枠<br>影響なし</div>
    <div class="feature">手数料<strong>2%〜</strong></div>
  </div>

  <svg class="abs scheme" viewBox="0 0 420 118" aria-label="取引先・お客様・ファクタリング会社の資金の流れ">
    <g fill="#1a1a1a">
      <rect x="14" y="16" width="40" height="62"/>
      <g fill="#fff"><rect x="20" y="24" width="8" height="8"/><rect x="40" y="24" width="8" height="8"/><rect x="20" y="40" width="8" height="8"/><rect x="40" y="40" width="8" height="8"/><rect x="20" y="56" width="8" height="8"/><rect x="40" y="56" width="8" height="8"/></g>
      <circle cx="196" cy="30" r="12"/>
      <path d="M176 74 Q176 46 196 46 Q216 46 216 74 Z"/>
      <rect x="330" y="30" width="64" height="44" rx="4"/>
    </g>
    <g stroke="#1a1a1a" stroke-width="2" fill="#1a1a1a">
      <line x1="64" y1="30" x2="164" y2="30"/><path d="M164 25 L172 30 L164 35 Z"/>
      <line x1="170" y1="62" x2="72" y2="62"/><path d="M72 57 L64 62 L72 67 Z"/>
      <line x1="226" y1="30" x2="318" y2="30"/><path d="M318 25 L326 30 L318 35 Z"/>
      <line x1="324" y1="62" x2="234" y2="62"/><path d="M234 57 L226 62 L234 67 Z"/>
    </g>
    <g font-family="Noto Sans JP, sans-serif" font-size="10" fill="#1a1a1a" text-anchor="middle">
      <text x="114" y="22">①請求書発行</text>
      <text x="114" y="80">④売掛金入金</text>
      <text x="276" y="22">②売掛債権譲渡</text>
      <text x="276" y="80">③現金化</text>
    </g>
    <g font-family="Noto Sans JP, sans-serif" font-size="12" font-weight="700" fill="#1a1a1a" text-anchor="middle">
      <text x="34" y="98">取引先</text>
      <text x="196" y="98">お客様</text>
      <text x="362" y="98">ファクタリング</text>
      <text x="362" y="113">会社</text>
    </g>
  </svg>

  <div class="abs office-photo" role="img" aria-label="相談窓口で担当者と話す女性の写真"></div>
  <div class="abs brand-strip"><span class="dot"></span>さくらもち舎</div>

  <div class="abs footer-rule"></div>
  <p class="abs company">さくらもち舎<small>(桜餅舎)</small></p>
  <p class="abs address">〒100-0000 東京都桜区花見町1-2-3 花見ビル3階</p>
  <p class="abs contact-band">お気軽にお問い合わせください</p>
  <p class="abs phone">0120-000-123</p>
</div>
</body>
</html>
```